Companybrochure for Consulting & Financing Firm

I need to have a Company Brochure asap for our company. We have a website that describes what we do, but we need also a brochure, that can be sent by PDF of eventually be printed as well.

The brochure should be short but nice and appealing to the customers.

We provide professional management consulting and help our customers to get finance for very diferent projects. Our business has a lot to do with personal relations, but also we are very professional in the way we work and how develop the solutions for our clients. Our clients are mainly government-owned firm, but also private trading companies and wealthy private investors.

Our customers are mainly in Latin America, but the company is headquater is in Switzerland. We are opening offices in Panama and Caracas, this should be easaly be adabtable later.

Please have a look at our website www.brevalto.ch. In the brochure, we would segment our services in 1.) Project Developments 2.) Management Conulting 3.) Investment Management and 4.) Finance Solutions.

Also do have a look at www.brevalto.ch
(Click E for the English version)

I managed to put the Mock-Up to the Website.
It is actually not really a mock-up, it is a version I have designed myself.
Well as I am not a designer, I hope you can make it much better.
The content however is what I would put in any other design as well.

Target Market(s)

Top Management, Investors, Entrepreneurs, Government Officials

Industry/Entity Type

Management Consulting

Requirements
Must have
• Design should reflect this image elements:

We are entrepreneurs.
We are comitted to get things done.
We work closely with the client side by side.
We are a professional partner.
We are not afraid of delivering unconventional solutions.
We look at the problem from various angles.
We analyse, develop solutions and implent results.
Should not have
• Typical US-American style elements. We do not want to give the impression of being a US company.

We do not want to appear to be neo-liberal. We are a politically neutral professional consulting firm.

```html
<!DOCTYPE html>
<html lang="en">
<head>
<meta charset="utf-8">
<title>Brevalto AG – Services</title>
<link href="https://fonts.googleapis.com/css2?family=Arimo:wght@400;700&display=swap" rel="stylesheet">
<style>
  :root {
    --navy: #22406f;
    --ink: #23386a;
    --panel: #e1e0e4;
    --paper: #ffffff;
    --sky-top: #5c8fd0;
    --sky-low: #c9b79c;
    --sea-top: #5b6166;
    --sea-low: #b9bdb6;
    --leaf-a: #4b6a2c;
    --leaf-b: #a8a36a;
  }
  html, body { margin: 0; padding: 0; overflow: hidden; }
  body { width: 1200px; height: 729px; position: relative; background: var(--paper);
         font-family: "Arimo", Arial, sans-serif; color: var(--ink); }
  .band { position: absolute; left: 0; width: 1200px; background: var(--navy); }
  .band--top { top: 26px; height: 74px; }
  .band--bottom { top: 707px; height: 22px; }
  .panel { position: absolute; background: var(--panel); }
  .panel--project { left: 0; top: 124px; width: 596px; height: 183px; }
  .panel--investment { left: 596px; top: 124px; width: 604px; height: 269px; }
  .photo { position: absolute; }
  .photo--antennas { left: 14px; top: 5px; width: 574px; height: 116px; border-radius: 4px;
    background: linear-gradient(180deg, var(--sky-top) 0%, #9fc0e6 45%, #8a8896 65%, var(--sky-low) 100%); }
  .photo--sails { left: 19px; top: 343px; width: 568px; height: 100px;
    background: linear-gradient(180deg, var(--sea-top) 0%, #7c8185 55%, var(--sea-low) 100%); }
  .photo--flower { left: 611px; top: 396px; width: 579px; height: 94px;
    background: linear-gradient(90deg, var(--leaf-a) 0%, #7d8a48 55%, var(--leaf-b) 80%, #c98aa0 100%); }
  .brand { position: absolute; left: 439px; top: 18px; font-size: 13px; font-weight: 700; color: #ffffff; margin: 0; }
  .section { position: absolute; }
  .section h2 { margin: 0 0 8px; font-size: 18px; font-weight: 700; color: var(--ink); }
  .section p { margin: 0; font-size: 15px; line-height: 19px; }
  .section p + p { margin-top: 19px; }
  .project { left: 32px; top: 139px; width: 558px; }
  .project .indent { margin-top: 14px; padding-left: 74px; }
  .project .lead { font-size: 19px; line-height: 22px; margin-top: 18px; margin-left: -2px; }
  .investment { left: 658px; top: 129px; width: 530px; }
  .investment .gap { margin-top: 30px; }
  .consulting { left: 32px; top: 453px; width: 558px; }
  .consulting p.just { text-align: justify; }
  .consulting .principle { margin-top: 0; padding-left: 286px; }
  .consulting .principle-intro { margin-top: 19px; }
  .finance { left: 658px; top: 497px; width: 530px; }
</style>
</head>
<body>
  <div class="band band--top"></div>
  <div class="photo photo--antennas" role="img" aria-label="Photograph of a row of large radio telescope dishes in a desert under a blue sky"></div>
  <p class="brand">Brevalto AG</p>

  <div class="panel panel--project"></div>
  <div class="panel panel--investment"></div>

  <section class="section project">
    <h2>&gt;&gt; Project Development</h2>
    <p>Sometimes a project with high potential has to be developed before its economic value becomes apparent.</p>
    <p class="indent" style="margin-top:14px">In such situations, we participate financially in the project and commit ourselves as entrepreneurs together with the owners.</p>
    <p class="lead">We also take care of project management.</p>
  </section>

  <section class="section investment">
    <h2>&gt;&gt; Investment Management</h2>
    <p>Brevalto has a clear business-like approach to investments. We only engage in those projects or companies with which we have a strong relationship.</p>
    <p style="margin-top:12px">That is why we are also willing to take an entrepreneurial risk in the companies we invest in. We participate with our own capital and assume functions in the company's management.</p>
    <p class="gap">Brevalto currently holds shares in seven SMEs; four of these to 100%. Participation is on equal terms, and two of of the companies we are minority shareholders.</p>
  </section>

  <div class="photo photo--sails" role="img" aria-label="Photograph of sailing boats with colourful sails racing on grey water"></div>
  <div class="photo photo--flower" role="img" aria-label="Photograph of a butterfly resting on a pink flower against green foliage"></div>

  <section class="section consulting">
    <h2>&gt;&gt; Management Consulting</h2>
    <p class="just">We elaborate solutions together with our customers and business partners by assisting owners and top management in structured decision making.</p>
    <p class="principle-intro">We work goal-oriented following the principle:</p>
    <p class="principle" style="margin-top:5px">&gt;Analysis &gt;&gt; Solutions &gt;&gt;&gt; Results.</p>
    <p class="just" style="margin-top:16px">Our consulting team members do all have many years of experience from previous assignments at leading international management consulting companies and are familiar with methodologies used in management consulting. We complete the team of consultants with the appropriate subject matter experts.</p>
  </section>

  <section class="section finance">
    <h2>&gt;&gt; Finance Solutions</h2>
    <p>Financing growth opportunities sometimes calls for an entrepreneurial perspective, which is often not found in the traditional banking world.</p>
    <p style="margin-top:13px">That is why we have committed ourselves to developing financing solutions for unconventional requirements. To do so, we often work with partners with complementary subject matter expertise and geographical coverage.</p>
    <p style="margin-top:13px">This gives us the flexibility to create innovative solutions – solutions that meet our clients' special needs.</p>
  </section>

  <div class="band band--bottom"></div>
</body>
</html>
```